Bramwell Dental personal information forms

We are a Dental Practice that require an update to our information forms, there are 3 versions of it.
I will attach our old ones, we need to keep the same information on there, we just want them to look better and use our current logo and colours.
Our website is www.bramwelldental-example.net
Our facebook is www.facebook.com/bramwelldentalkestonwalk/
..................................................................................................

Target Market(s)

Everyone, easy to read

Industry/Entity Type

Dental Clinic

Colors
0692cd
34a6d7
cee9f5
ffffff
0255a3
3276b5

Requirements
Must have
• Logo
• Our colours
• same information as the uploaded versions
Should not have
• any other colour besides the blues, black and white

```html
<!DOCTYPE html>
<html lang="en">
<head>
<meta charset="utf-8">
<title>Bramwell Dental – Medical History Form</title>
<link rel="stylesheet" href="https://fonts.googleapis.com/css2?family=Lato:ital,wght@0,400;0,700;0,900;1,400&display=swap">
<style>
  :root {
    --blue-deep: #0255a3;
    --blue-main: #0692cd;
    --blue-mid: #3276b5;
    --blue-light: #34a6d7;
    --blue-pale: #cee9f5;
    --field: #e6e9ec;
    --rule: #d3d7db;
    --ink: #1a1a1a;
    --white: #ffffff;
  }
  * { box-sizing: border-box; margin: 0; padding: 0; }
  html, body { width: 781px; height: 1200px; overflow: hidden; background: var(--white); }
  body { font-family: "Lato", Arial, sans-serif; color: var(--ink); position: relative; }

  .header {
    position: absolute; left: 0; top: 0; width: 781px; height: 104px;
    background: linear-gradient(180deg, var(--blue-main) 0%, var(--blue-mid) 60%, var(--blue-deep) 100%);
  }
  .header-rule { position: absolute; left: 0; top: 104px; width: 781px; height: 6px;
    background: linear-gradient(180deg, var(--blue-light), var(--blue-main)); border-top: 2px solid var(--white); }
  .brand { position: absolute; left: 40px; top: 33px; color: var(--white); font-weight: 700; font-size: 32px; line-height: 1; white-space: nowrap; }
  .contact { position: absolute; right: 24px; top: 24px; color: var(--white); }
  .contact-phone { display: flex; align-items: center; gap: 12px; font-size: 27px; font-weight: 700; letter-spacing: 0.5px; }
  .contact-web { display: flex; align-items: center; gap: 20px; font-size: 16px; margin-top: 10px; padding-left: 4px; }

  .practitioners { position: absolute; left: 22px; top: 174px; color: var(--blue-deep); font-weight: 700; font-size: 13.5px; line-height: 1.2; }
  .sticker { position: absolute; left: 472px; top: 158px; width: 287px; height: 62px;
    border: 1px solid #e2e4e6; display: flex; align-items: center; justify-content: center;
    font-style: italic; font-size: 13px; }

  .welcome { position: absolute; left: 22px; top: 258px; color: var(--blue-main); font-size: 13px; }
  .intro { position: absolute; left: 22px; top: 277px; width: 740px; font-size: 12.4px; line-height: 1.38; }
  .intro strong { font-weight: 900; }

  .question { position: absolute; left: 22px; width: 737px; border-top: 1px solid var(--rule); font-size: 11.6px; line-height: 1.4; }
  .question-text { display: flex; justify-content: space-between; padding: 6px 8px 0 10px; }
  .question-text .yn { font-weight: 700; font-size: 12px; }
  .answer-field { height: 20px; background: var(--field); margin-top: 6px; }

  .conditions-title { position: absolute; left: 32px; top: 560px; font-size: 11.6px; }
  .conditions { position: absolute; left: 42px; top: 590px; display: flex; font-size: 11.2px; }
  .conditions ul { list-style: none; width: 236px; }
  .conditions li { display: flex; align-items: center; gap: 10px; height: 17.6px; }
  .tick-box { width: 8px; height: 8px; border-left: 2px solid var(--ink); border-bottom: 2px solid var(--ink); }

  .declaration { position: absolute; left: 22px; top: 1016px; width: 740px; font-weight: 900; font-size: 11.6px; line-height: 1.35; }
  .sign-row { position: absolute; left: 22px; top: 1066px; display: flex; align-items: flex-end; font-size: 11px; }
  .sign-line { display: inline-block; width: 132px; border-bottom: 1px solid #888; margin: 0 40px 0 8px; height: 10px; }
  .date-line { display: inline-block; width: 132px; border-bottom: 1px solid #888; margin-left: 10px; height: 10px; }

  .footer { position: absolute; left: 0; top: 1152px; width: 781px; height: 48px;
    background: linear-gradient(180deg, var(--blue-main), var(--blue-deep));
    border-top: 3px solid var(--blue-light);
    color: var(--white); font-size: 22px; display: flex; align-items: center; justify-content: center; }
</style>
</head>
<body>
  <header class="header">
    <div class="brand">Bramwell Dental</div>
    <div class="contact">
      <div class="contact-phone">
        <svg width="26" height="26" viewBox="0 0 26 26" aria-hidden="true">
          <circle cx="13" cy="13" r="11.5" fill="none" stroke="#fff" stroke-width="2"/>
          <path d="M9 7.5c-.8.4-1.6 1.4-1.3 3 .6 3.4 4.2 7 7.6 7.6 1.6.3 2.6-.5 3-1.3l-2.3-1.9-1.4 1c-1.6-.6-3.5-2.5-4.1-4.1l1-1.4z" fill="#fff"/>
        </svg>
        08 5550 1947
      </div>
      <div class="contact-web">
        <svg width="12" height="12" viewBox="0 0 12 12" aria-hidden="true">
          <circle cx="6" cy="6" r="5.3" fill="none" stroke="#fff" stroke-width="1.2"/>
          <ellipse cx="6" cy="6" rx="2.3" ry="5.3" fill="none" stroke="#fff" stroke-width="1"/>
          <line x1="0.7" y1="6" x2="11.3" y2="6" stroke="#fff" stroke-width="1"/>
        </svg>
        www.bramwelldental-example.net
      </div>
    </div>
  </header>
  <div class="header-rule"></div>

  <div class="practitioners">Dr. Peter Halloran &amp; Dr. Simon Achterberg<br>Dental Surgeons</div>
  <div class="sticker">Affix patient sticker here.</div>

  <p class="welcome">Welcome back to our practice!</p>
  <p class="intro"><strong>THIS INFORMATION IS CONFIDENTIAL</strong> and is necessary to enable us to offer you <strong>THE BEST POSSIBLE</strong> CARE.It is now mandatory to have a written updated medical history every 2 years and we would appreciate your time in thoroughly completing this form.</p>

  <section class="question" style="top:406px">
    <div class="question-text"><span>Are you currently or have you taken any prescribed medication or dietary supplements in the last 12 months?<br>(If YES please list below)</span><span class="yn">YES/NO</span></div>
    <div class="answer-field" style="margin-top:4px"></div>
  </section>
  <section class="question" style="top:470px">
    <div class="question-text"><span>Allergies / Reactions?<br>(If YES please list below)</span><span class="yn">YES/NO</span></div>
    <div class="answer-field" style="margin-top:4px"></div>
  </section>

  <p class="conditions-title">Have you ever had or are you suffering from any of the following? Please tick any that apply :</p>
  <div class="conditions">
    <ul>
      <li><span class="tick-box"></span>Rheumatic fever</li>
      <li><span class="tick-box"></span>Epilepsy</li>
      <li><span class="tick-box"></span>Asthma</li>
      <li><span class="tick-box"></span>Tuberculosis</li>
      <li><span class="tick-box"></span>Radiation Therapy</li>
      <li><span class="tick-box"></span>Dizziness, fainting</li>
      <li><span class="tick-box"></span>Hepatitis A B or C</li>
      <li><span class="tick-box"></span>Recent eye surgery</li>
    </ul>
    <ul>
      <li><span class="tick-box"></span>Diabetes</li>
      <li><span class="tick-box"></span>kidney disease</li>
      <li><span class="tick-box"></span>Heart attack</li>
      <li><span class="tick-box"></span>High Blood Pressure</li>
      <li><span class="tick-box"></span>Bleeding problems</li>
      <li><span class="tick-box"></span>Artificial joints</li>
      <li><span class="tick-box"></span>Respiratory Problems</li>
    </ul>
    <ul>
      <li><span class="tick-box"></span>HIV Positive</li>
      <li><span class="tick-box"></span>High cholesterol</li>
      <li><span class="tick-box"></span>Cancer</li>
      <li><span class="tick-box"></span>Pace-maker</li>
      <li><span class="tick-box"></span>Osteoporosis</li>
      <li><span class="tick-box"></span>Heart rate problems</li>
      <li><span class="tick-box"></span>Heart murmur</li>
    </ul>
  </div>

  <section class="question" style="top:772px; border-top:none">
    <div class="question-text"><span>Do you have any disease,condition or problem not lited above?</span><span class="yn">YES/NO</span></div>
    <div class="answer-field" style="margin-top:2px"></div>
  </section>
  <section class="question" style="top:819px; border-top:none">
    <div class="question-text"><span>Have you had surgery or been to hospital in the last 5 years? (If YES,Please give details)</span><span class="yn">YES/NO</span></div>
    <div class="answer-field" style="margin-top:2px"></div>
  </section>
  <section class="question" style="top:866px; border-top:none">
    <div class="question-text"><span>For Women:Are you pregnant? (If YES, How many months?)</span><span class="yn">YES/NO</span></div>
    <div class="answer-field" style="margin-top:2px"></div>
  </section>
  <section class="question" style="top:912px; border-top:none">
    <div class="question-text"><span>Do you currently or have you ever smoked?</span><span class="yn">YES/NO</span></div>
    <div class="answer-field" style="margin-top:2px"></div>
  </section>

  <p class="declaration">The information that I have provided is to the best of my knowledge true and I understand that is my responsibility to inform of any changes in my medical status.</p>
  <div class="sign-row">Patient/Parent/Person Responsible signature:<span class="sign-line"></span><strong>Date:</strong><span class="date-line"></span></div>

  <footer class="footer">www.bramwelldental-example.net</footer>
</body>
</html>
```